Cobbleford Works New Website

Custom Wood Cabinetry and Precisions Wood Cutting website. I have created a pdf document with all the specs for the project and attached it. I am just typing stuff in here so it stops telling me my description is too short. Their once was a man from Nantucket.. he used to pee in a bucket.. roses are red, cardinals are birds, i wish they didn't require 300 words.
Number of Pages Required
1 page

```html
<!DOCTYPE html>
<html lang="en">
<head>
<meta charset="utf-8">
<title>Cobbleford Works — Custom Cabinetry and Woodworking</title>
<link rel="stylesheet" href="https://fonts.googleapis.com/css2?family=Montserrat:wght@400;500;600;700;800;900&family=Zilla+Slab:wght@700&display=swap">
<style>
:root{
  --brown-dark:#4c2813;
  --brown:#5b3019;
  --brown-mid:#7b4a2c;
  --brown-deep:#3f200f;
  --accent:#9a5228;
  --cream:#f6ece4;
  --white:#ffffff;
  --text:#3a2a20;
  --muted:#6b5a50;
  --wood-1:#8a5a32;
  --wood-2:#c79b68;
}
*{box-sizing:border-box;margin:0;padding:0}
html,body{width:1200px;height:3536px;overflow:hidden}
body{position:relative;background:var(--white);font-family:'Montserrat',sans-serif;color:var(--text)}
.abs{position:absolute}
a{color:inherit;text-decoration:none}

/* header */
.brand{left:141px;top:22px;display:flex;align-items:center;gap:10px}
.brand-dot{width:22px;height:22px;border-radius:50%;background:var(--brown)}
.brand-name{font-weight:800;font-size:27px;color:var(--brown);letter-spacing:.5px}
.contact-item{display:flex;gap:14px;align-items:center;top:32px}
.contact-item svg{width:32px;height:32px}
.contact-label{font-size:11px;color:var(--muted);letter-spacing:.5px}
.contact-value{font-size:14px;font-weight:700;color:var(--accent);margin-top:3px}

.navbar{left:0;top:105px;width:1200px;height:46px;background:var(--brown-dark)}
.nav-link{top:0;line-height:46px;font-size:12px;color:#f3e5da}
.nav-link.active{font-weight:700;color:#fff;text-decoration:underline;text-underline-offset:4px}
.nav-quote{left:932px;top:7px;width:127px;height:32px;border:1.5px solid #fff;border-radius:16px;color:#fff;font-size:12px;font-weight:600;display:flex;align-items:center;justify-content:center}

/* hero */
.hero{left:0;top:151px;width:1200px;height:540px;background:linear-gradient(180deg,#8a5a34 0%,#6a4124 45%,#a67a4d 70%,#5e3a20 100%)}
.hero-shade{left:0;top:151px;width:1200px;height:540px;background:rgba(30,15,5,.35)}
.hero-title{left:300px;top:370px;width:600px;text-align:center;color:#fff;font-weight:800;font-size:30px;line-height:41px;letter-spacing:.5px}
.hero-title small{font-size:22px;font-weight:500}
.btn-ghost{border:1.5px solid #fff;color:#fff;border-radius:20px;font-size:12px;font-weight:500;display:flex;align-items:center;justify-content:center}
.btn-solid{background:var(--brown-dark);color:#fff;border-radius:20px;font-size:12px;font-weight:500;display:flex;align-items:center;justify-content:center;box-shadow:0 2px 0 #2a1409}

/* features */
.features{left:0;top:680px;width:1200px;height:116px;background:var(--cream)}
.feature{top:694px;display:flex;gap:14px;width:290px}
.feature svg{width:60px;height:54px;flex:none}
.feature h3{font-size:14px;font-weight:700;color:var(--accent)}
.feature p{font-size:11.5px;line-height:20px;color:var(--muted);margin-top:2px}

.section-title{left:0;width:1200px;text-align:center;font-weight:900;font-size:42px;color:var(--brown);letter-spacing:.5px}
.rule{height:2px;background:var(--brown)}
.rule-accent{width:26px;height:3px;background:var(--accent)}

/* services */
.service-card{top:960px;width:286px;height:226px;background:#fff;box-shadow:0 1px 6px rgba(0,0,0,.14)}
.service-img{width:286px;height:176px}
.service-label{text-align:center;font-size:13.5px;font-weight:700;color:var(--accent);margin-top:17px;letter-spacing:.3px}

/* about */
.about-band{left:0;top:1262px;width:1200px;height:650px;background:var(--cream)}
.badge-box{left:141px;top:1355px;width:84px;height:125px;border:12px solid #fff;border-right-width:0}
.badge-num{left:170px;top:1362px;font-weight:900;font-size:92px;color:var(--brown);letter-spacing:-4px}
.years{left:300px;top:1365px;font-weight:900;font-size:43px;line-height:54px;color:var(--brown)}
.about-heading{left:141px;top:1496px;font-family:'Zilla Slab',serif;font-size:39px;color:var(--brown-dark)}
.about-copy{left:141px;top:1585px;width:458px;font-size:11.6px;line-height:20.4px;color:var(--text)}
.about-photo{left:616px;top:1355px;width:417px;height:346px}
.about-frame{left:655px;top:1374px;width:377px;height:246px;border:1px solid rgba(255,255,255,.4)}
.about-inset{left:805px;top:1619px;width:254px;height:165px;background:#fff;padding:12px}

/* gallery */
.filter{top:2062px;height:48px;display:flex;align-items:center;justify-content:center;font-size:14px;color:var(--accent);border:1px solid var(--accent);background:#fff}
.filter.active{background:var(--brown-dark);color:#fff;border-color:var(--brown-dark)}
.tile{border:0}

/* cnc banner */
.cnc-photo{left:141px;top:2817px;width:918px;height:290px;background:linear-gradient(90deg,#8c6a4a 0%,#b8a080 40%,#5f6e86 60%,#c8b8a0 100%)}
.cnc-card{left:163px;top:2840px;width:376px;height:248px;background:rgba(255,255,255,.94)}
.cnc-inner{left:180px;top:2855px;width:342px;height:216px;border:1px solid var(--accent)}
.cnc-title{left:206px;top:2880px;font-weight:800;font-size:23px;line-height:32px;color:var(--brown)}

/* footer */
.footer{left:0;top:3178px;width:1200px;height:306px;background:var(--brown-mid)}
.copyright{left:0;top:3484px;width:1200px;height:52px;background:var(--brown-deep);color:#f2e4d8;font-size:11.5px;text-align:center;line-height:52px}
.foot-title{top:3264px;color:#fff;font-size:15.5px;font-weight:700;letter-spacing:.5px}
.foot-rule{top:3294px;height:1px;background:rgba(255,255,255,.45)}
.foot-list{list-style:none;top:3310px;color:#f7ebe2;font-size:12px}
.foot-list li{height:26px;display:flex;align-items:center;gap:12px}
.foot-list.bold{font-weight:600;font-size:11px}
.chev{font-size:12px;letter-spacing:-3px;color:#fff}
.social{top:3399px;width:30px;height:30px;border:1.5px solid #fff;border-radius:50%}
.subscribe{left:595px;top:3401px;width:428px;height:30px;background:#fff;border-radius:15px}
.subscribe span{position:absolute;left:14px;top:0;line-height:30px;font-size:11px;color:#8a7a70}
.subscribe-btn{left:898px;top:3401px;width:125px;height:30px;background:var(--brown-dark);border-radius:15px;color:#fff;font-size:12px;display:flex;align-items:center;justify-content:center}
.foot-brand{left:848px;top:3316px;display:flex;align-items:center;gap:8px}
</style>
</head>
<body>

<!-- header -->
<div class="abs brand"><span class="brand-dot"></span><span class="brand-name">Cobbleford Works</span></div>

<div class="abs contact-item" style="left:625px">
  <svg viewBox="0 0 32 32" fill="none" stroke="#9a5228" stroke-width="1.6"><path d="M4 13 16 4l12 9v15H4z"/><path d="M4 13l12 9 12-9"/><circle cx="16" cy="13" r="3.5"/></svg>
  <div><div class="contact-label">EMAIL</div><div class="contact-value">info@cobblefordworks.com</div></div>
</div>
<div class="abs contact-item" style="left:910px">
  <svg viewBox="0 0 32 32" fill="none" stroke="#9a5228" stroke-width="1.6"><path d="M8 4l5 6-3 3c2 4 5 7 9 9l3-3 6 5-3 4C15 28 4 17 4 7z"/></svg>
  <div><div class="contact-label">PHONE</div><div class="contact-value">123-456-7890</div></div>
</div>

<nav class="abs navbar">
  <a class="abs nav-link active" style="left:143px">Home</a>
  <a class="abs nav-link" style="left:210px">About</a>
  <a class="abs nav-link" style="left:280px">Services &nbsp;&#8964;</a>
  <a class="abs nav-link" style="left:382px">FAQs</a>
  <a class="abs nav-link" style="left:447px">Contact</a>
  <a class="abs nav-link" style="left:651px">&#128722;&#xFE0E; Cart</a>
  <a class="abs nav-link" style="left:735px">&#9786;&#xFE0E; Login</a>
  <a class="abs nav-link" style="left:823px">&#9786;&#xFE0E;+ Sign Up</a>
  <a class="abs nav-quote">Request A Quote</a>
</nav>

<!-- hero -->
<div class="abs hero" role="img" aria-label="Photo of a finished knotty wood custom kitchen with cabinets and a range"></div>
<div class="abs hero-shade"></div>
<h1 class="abs hero-title"><small>WE ARE</small> CUSTOM CABINETRY,<br>PRECISION WOOD CUTTING &amp;<br>CUSTOM WOOD ART <small>COMPANY.</small></h1>
<a class="abs btn-ghost" style="left:519px;top:511px;width:161px;height:38px">Request A Quote</a>

<!-- features -->
<div class="abs features"></div>
<svg class="abs" style="left:0;top:666px" width="1200" height="22" viewBox="0 0 1200 22" preserveAspectRatio="none"><path fill="#f6ece4" d="M0 14 40 9 80 15 130 8 180 13 240 7 300 14 360 9 420 15 480 8 540 13 600 9 660 15 720 8 780 13 840 7 900 14 960 9 1020 15 1080 8 1140 13 1200 9V22H0z"/></svg>
<svg class="abs" style="left:0;top:788px" width="1200" height="16" viewBox="0 0 1200 16" preserveAspectRatio="none"><path fill="#f6ece4" d="M0 0H1200V6L1150 11 1090 5 1030 12 970 6 900 11 840 5 780 12 720 6 650 11 590 5 520 12 460 6 400 11 340 5 280 12 220 6 150 11 90 5 30 12 0 7z"/></svg>

<div class="abs feature" style="left:141px">
  <svg viewBox="0 0 60 54" fill="none" stroke="#5b3019" stroke-width="2"><path d="M3 10h44l8 6-6 10 3 12-10 2-4 8-10-4H15L5 28z"/><text x="15" y="34" font-family="Montserrat" font-size="13" font-weight="700" fill="#9a5228" stroke="none">USA</text></svg>
  <div><h3>US Made</h3><p>Morbi ac quam consequat neqe volutpat venenatis quis augue.</p></div>
</div>
<div class="abs feature" style="left:490px">
  <svg viewBox="0 0 60 54" fill="none" stroke="#5b3019" stroke-width="2"><circle cx="22" cy="18" r="12"/><circle cx="22" cy="18" r="5"/><circle cx="36" cy="30" r="9"/><path d="M32 38l-4 14 8-4 8 4-4-14"/></svg>
  <div><h3>Quality Products</h3><p>Morbi ac quam consequat neqe volutpat venenatis quis augue.</p></div>
</div>
<div class="abs feature" style="left:805px">
  <svg viewBox="0 0 60 54" fill="none" stroke="#5b3019" stroke-width="2"><path d="M8 46 40 14M14 48 46 16M36 6l10 10M6 36l10 10"/><rect x="18" y="26" width="22" height="6" transform="rotate(-45 29 29)"/></svg>
  <div><h3>Talented Craftsmen</h3><p>Morbi ac quam consequat neqe volutpat venenatis quis augue.</p></div>
</div>

<!-- services -->
<h2 class="abs section-title" style="top:858px">OUR SERVICES</h2>
<div class="abs rule" style="left:545px;top:922px;width:110px;background:#c9b4a6;height:1px"></div>
<div class="abs rule-accent" style="left:587px;top:921px"></div>

<article class="abs service-card" style="left:141px">
  <div class="service-img" role="img" aria-label="Photo of a dark wood kitchen with granite island" style="background:linear-gradient(160deg,#4a2e1d,#7a5a42 60%,#b8aca0)"></div>
  <div class="service-label">CUSTOM CABINETRY</div>
</article>
<article class="abs service-card" style="left:457px">
  <div class="service-img" role="img" aria-label="Photo of a CNC bit carving a wood panel" style="background:linear-gradient(160deg,#6a5a4c,#9a8a78 55%,#5a4a3c)"></div>
  <div class="service-label">CNC PRECISION WOOD CUTTING</div>
</article>
<article class="abs service-card" style="left:773px">
  <div class="service-img" role="img" aria-label="Photo of a carved wooden flag and eagle art panel" style="background:linear-gradient(160deg,#8a7866,#6a5848 55%,#4a3a2c)"></div>
  <div class="service-label">CUSTOM WOOD ART PROJECTS</div>
</article>
<svg class="abs" style="left:599px;top:1035px" width="52" height="30" viewBox="0 0 52 30" fill="none" stroke="#fff" stroke-width="1.8"><path d="M2 15h34M30 9l6 6-6 6"/><circle cx="37" cy="15" r="13"/></svg>

<!-- about -->
<div class="abs about-band"></div>
<svg class="abs" style="left:0;top:1250px" width="1200" height="18" viewBox="0 0 1200 18" preserveAspectRatio="none"><path fill="#f6ece4" d="M0 12 60 7 120 13 190 6 250 12 320 7 380 13 450 6 510 12 580 7 640 13 710 6 770 12 840 7 900 13 970 6 1030 12 1100 7 1160 13 1200 9V18H0z"/></svg>
<svg class="abs" style="left:0;top:1905px" width="1200" height="18" viewBox="0 0 1200 18" preserveAspectRatio="none"><path fill="#f6ece4" d="M0 0H1200V7L1140 12 1080 5 1010 12 950 6 880 11 820 5 750 12 690 6 620 11 560 5 490 12 430 6 360 11 300 5 230 12 170 6 100 11 40 5 0 8z"/></svg>

<div class="abs badge-box"></div>
<div class="abs badge-num">25</div>
<div class="abs years">YEARS OF<br>EXPERIENCE</div>
<h2 class="abs about-heading">About Cobbleford Works</h2>
<div class="abs rule" style="left:141px;top:1555px;width:106px;background:#d2bdb0;height:1px"></div>
<div class="abs rule-accent" style="left:141px;top:1554px"></div>
<p class="abs about-copy">Lorem ipsum dolor sit amet, consectetuer adipiscing elit, sed diam nonummy nibh euismod tincidunt ut laoreet dolore magna aliquam erat volutpat. Ut wisi enim ad minim veniam, quis nostrud exerci tation ullamcorper suscipit lobortis nisl ut aliquip ex ea commodo consequat. Duis autem vel eum iriure dolor in hendrerit in vulputate velit esse molestie consequat, vel illum dolore eu feugiat nulla facilisis at vero eros et accumsan et iusto odio dignissim qui blandit praesent luptatum zzril delenit augue duis dolore te feugait nulla facilisi.</p>
<a class="abs btn-solid" style="left:141px;top:1776px;width:126px;height:39px">Read More</a>
<a class="abs btn-solid" style="left:281px;top:1776px;width:161px;height:39px">Request A Quote</a>

<div class="abs about-photo" role="img" aria-label="Photo of a bright wood kitchen with stainless appliances" style="background:linear-gradient(160deg,#6a4a2e,#9a7450 50%,#7a6a5a)"></div>
<div class="abs about-frame"></div>
<div class="abs about-inset"><div role="img" aria-label="Distressed flag artwork" style="width:230px;height:141px;background:linear-gradient(180deg,#d9d2cc 0%,#e8e2dc 65%,#d2705e 80%,#e8e2dc 100%)"></div></div>

<!-- gallery -->
<h2 class="abs section-title" style="top:1974px">WORK GALLERY</h2>
<div class="abs rule" style="left:545px;top:2038px;width:110px;background:#c9b4a6;height:1px"></div>
<div class="abs rule-accent" style="left:587px;top:2037px"></div>

<a class="abs filter active" style="left:233px;width:110px">All</a>
<a class="abs filter" style="left:352px;width:144px">Newest Creations</a>
<a class="abs filter" style="left:505px;width:235px">CNC Precision Wood Cutting</a>
<a class="abs filter" style="left:749px;width:218px">Custom Wood Art Projects</a>

<div class="abs tile" style="left:141px;top:2146px;width:229px;height:247px;background:linear-gradient(170deg,#a07040,#7a5232 60%,#3a2a20)" role="img" aria-label="Photo of rustic kitchen cabinets around a range"></div>
<div class="abs tile" style="left:389px;top:2146px;width:422px;height:247px;background:radial-gradient(ellipse at center,#e2b27a,#b0733e 70%,#6a4428)" role="img" aria-label="Photo of an engraved wooden family sign with trees"></div>
<div class="abs tile" style="left:829px;top:2146px;width:230px;height:247px;background:linear-gradient(170deg,#9a8a72,#c8b89c 55%,#5a6a86)" role="img" aria-label="Photo of a cut plywood dinosaur model on a CNC table"></div>
<div class="abs tile" style="left:141px;top:2411px;width:229px;height:247px;background:linear-gradient(170deg,#8a6a4e,#4a2a18 55%,#7a6050)" role="img" aria-label="Photo of a dark wood bench seat"></div>
<div class="abs tile" style="left:389px;top:2411px;width:229px;height:247px;background:linear-gradient(170deg,#d8ccbc,#a87a4a 45%,#7a5030)" role="img" aria-label="Photo of tall built-in wooden shelves with a ladder"></div>
<div class="abs tile" style="left:636px;top:2411px;width:423px;height:247px;background:linear-gradient(90deg,#a8845c 0%,#e8e8e6 20%,#f0f0ee 75%,#c8c6c2 100%)" role="img" aria-label="Photo of white built-in mudroom cabinets with bench"></div>
<svg class="abs" style="left:574px;top:2255px" width="52" height="30" viewBox="0 0 52 30" fill="none" stroke="#fff" stroke-width="1.8"><path d="M2 15h34M30 9l6 6-6 6"/><circle cx="37" cy="15" r="13"/></svg>

<a class="abs btn-solid" style="left:519px;top:2693px;width:161px;height:39px">Request A Quote</a>

<!-- cnc banner -->
<div class="abs cnc-photo" role="img" aria-label="Photo of a CNC router table in a woodworking shop"></div>
<div class="abs cnc-card"></div>
<div class="abs cnc-inner"></div>
<h2 class="abs cnc-title">SPECILIZING IN CNC<br>PRECISION WOOD<br>CUTTING SERVICE ALSO</h2>
<a class="abs btn-solid" style="left:206px;top:3002px;width:161px;height:39px">Request A Quote</a>

<!-- footer -->
<div class="abs footer"></div>
<svg class="abs" style="left:0;top:3165px" width="1200" height="18" viewBox="0 0 1200 18" preserveAspectRatio="none"><path fill="#7b4a2c" d="M0 12 50 6 110 13 170 7 230 12 300 5 360 13 420 7 490 12 550 6 610 13 680 7 740 12 800 5 870 13 930 7 990 12 1060 6 1120 13 1200 8V18H0z"/></svg>

<h3 class="abs foot-title" style="left:141px">QUICK LINKS</h3>
<div class="abs foot-rule" style="left:141px;width:107px"></div>
<ul class="abs foot-list" style="left:141px">
  <li><span class="chev">&rsaquo;&rsaquo;</span><span style="font-weight:700;color:#fff;text-decoration:underline">Home</span></li>
  <li><span class="chev">&rsaquo;&rsaquo;</span>About</li>
  <li><span class="chev">&rsaquo;&rsaquo;</span>Services</li>
  <li><span class="chev">&rsaquo;&rsaquo;</span>FAQs</li>
  <li><span class="chev">&rsaquo;&rsaquo;</span>Contact</li>
</ul>

<h3 class="abs foot-title" style="left:325px">SERVICES</h3>
<div class="abs foot-rule" style="left:325px;width:213px"></div>
<ul class="abs foot-list bold" style="left:325px">
  <li><span class="chev">&rsaquo;&rsaquo;</span>Custom Cabinetry</li>
  <li><span class="chev">&rsaquo;&rsaquo;</span>CNC Precision Wood Cutting</li>
  <li><span class="chev">&rsaquo;&rsaquo;</span>Custom Wood Art Projects</li>
</ul>
<span class="abs social" style="left:327px" aria-label="Social profile"></span>
<span class="abs social" style="left:365px" aria-label="Social profile"></span>
<span class="abs social" style="left:404px" aria-label="Social profile"></span>
<span class="abs social" style="left:442px" aria-label="Social profile"></span>

<h3 class="abs foot-title" style="left:595px">CONTACT DETAILS</h3>
<div class="abs foot-rule" style="left:595px;width:160px"></div>
<ul class="abs foot-list bold" style="left:595px;font-size:11.5px">
  <li><svg width="16" height="14" viewBox="0 0 16 14" fill="none" stroke="#fff" stroke-width="1.2"><path d="M1 6 8 1l7 5v7H1z"/><path d="M1 6l7 5 7-5"/></svg>info@cobblefordworks.com</li>
  <li style="margin-top:6px"><svg width="16" height="14" viewBox="0 0 16 14" fill="none" stroke="#fff" stroke-width="1.2"><path d="M3 1l3 3-2 2c1 2 3 4 5 5l2-2 3 3-2 2C7 14 0 7 1 3z"/></svg>123-456-7890</li>
</ul>
<div class="abs subscribe"><span>Email Address</span></div>
<a class="abs subscribe-btn">Subscribe</a>

<div class="abs foot-brand"><span class="brand-dot" style="background:#fff;width:18px;height:18px"></span><span class="brand-name" style="color:#fff;font-size:22px">Cobbleford Works</span></div>

<div class="abs copyright">Copyright © 2021 Cobbleford Works. All Rights Reserved.</div>

</body>
</html>
```